New Business Card Design*

We are a recruitment company based in Norwich/Cambridge England.
I have included our company logo which we want to remain the same.

What we are looking for is a new creative Business card which will really stand out!!

Contact Information for Business Card

Harriet Vance
email: Harriet@brelvix.co.uk
Address: Tolworth House
Ashgrove Innovation Park
Pelham Road
Norwich
KT9 3QD
Tel:01632 960418

```html
<!DOCTYPE html>
<html lang="en">
<head>
<meta charset="utf-8">
<title>Brelvix Business Card</title>
<link rel="stylesheet" href="https://fonts.googleapis.com/css2?family=Open+Sans:wght@400;600;700&display=swap">
<style>
  :root {
    --bg: #2b2b2b;
    --green: #9fd20f;
    --grey: #8f8d91;
    --grey-light: #c9c8cb;
    --white: #ffffff;
  }
  * { box-sizing: border-box; margin: 0; padding: 0; }
  html, body { width: 1200px; height: 900px; overflow: hidden; }
  body {
    background: var(--bg);
    font-family: "Open Sans", Arial, sans-serif;
    position: relative;
  }
  .card {
    position: absolute;
    width: 540px;
    height: 310px;
    border-radius: 18px;
    overflow: hidden;
  }
  .card-front { left: 100px; top: 100px; background: var(--white); }
  .card-back { left: 560px; top: 490px; background: var(--green); }
  .wave { position: absolute; inset: 0; width: 100%; height: 100%; }

  .brand { position: absolute; display: flex; align-items: center; }
  .brand-dot { border-radius: 50%; flex: none; }
  .brand-text { display: flex; flex-direction: column; }
  .brand-name { font-weight: 600; line-height: 1; }
  .brand-tagline { letter-spacing: 0.22em; font-weight: 400; }

  .card-front .brand { left: 30px; top: 100px; gap: 10px; }
  .card-front .brand-dot { width: 44px; height: 44px; background: var(--grey); }
  .card-front .brand-name { font-size: 36px; color: var(--green); }
  .card-front .brand-tagline { font-size: 7px; color: var(--grey); margin-top: 3px; margin-left: 2px; }

  .contact {
    position: absolute;
    right: 22px;
    top: 56px;
    text-align: right;
    color: var(--white);
    font-size: 12px;
    line-height: 18px;
  }
  .contact-name { font-weight: 700; font-size: 14px; margin-bottom: 4px; }
  .contact-line { display: flex; justify-content: flex-end; align-items: center; gap: 6px; }
  .contact-line svg { width: 10px; height: 10px; flex: none; }
  .contact-address { margin-top: 10px; }

  .card-back .brand { left: 50%; top: 50%; transform: translate(-50%, -50%); gap: 18px; }
  .card-back .brand-dot { width: 72px; height: 72px; background: var(--white); }
  .card-back .brand-name { font-size: 62px; color: var(--white); }
  .card-back .brand-tagline { font-size: 12px; color: var(--white); margin-top: 4px; margin-left: 4px; }
</style>
</head>
<body>

<section class="card card-front">
  <svg class="wave" viewBox="0 0 540 310" preserveAspectRatio="none" aria-hidden="true">
    <path d="M560,18 C430,18 350,38 298,108 C255,168 248,238 176,260 C120,278 50,272 0,252 L0,310 L560,310 Z" fill="var(--grey-light)"/>
    <path d="M560,28 C440,28 362,48 310,118 C268,178 260,248 188,270 C130,288 55,284 0,266 L0,310 L560,310 Z" fill="var(--green)"/>
  </svg>

  <div class="brand">
    <span class="brand-dot"></span>
    <div class="brand-text">
      <span class="brand-name">Brelvix</span>
      <span class="brand-tagline">Technology Recruitment</span>
    </div>
  </div>

  <div class="contact">
    <p class="contact-name">Harriet Vance</p>
    <p class="contact-line">01632 960418
      <svg viewBox="0 0 12 12"><path d="M3 1 L5 3 L4 5 Q5 7 7 8 L9 7 L11 9 L9.5 11 Q5 11 2.5 7 Q1 4 3 1 Z" fill="var(--white)"/></svg>
    </p>
    <p class="contact-line">Harriet@brelvix.co.uk
      <svg viewBox="0 0 12 12"><rect x="1" y="2.5" width="10" height="7" fill="var(--white)"/><path d="M1 2.5 L6 6.5 L11 2.5" fill="none" stroke="var(--green)" stroke-width="1"/></svg>
    </p>
    <p class="contact-line">www.brelvix.co.uk
      <svg viewBox="0 0 12 12"><circle cx="6" cy="6" r="5" fill="none" stroke="var(--white)" stroke-width="1.2"/><ellipse cx="6" cy="6" rx="2" ry="5" fill="none" stroke="var(--white)" stroke-width="1"/><line x1="1" y1="6" x2="11" y2="6" stroke="var(--white)" stroke-width="1"/></svg>
    </p>
    <p class="contact-address">Tolworth House Ashgrove Innovation Park<br>Pelham Road Norwich KT9 3QD</p>
  </div>
</section>

<section class="card card-back">
  <div class="brand">
    <span class="brand-dot"></span>
    <div class="brand-text">
      <span class="brand-name">Brelvix</span>
      <span class="brand-tagline">Technology Recruitment</span>
    </div>
  </div>
</section>

</body>
</html>
```